Sponsorship and registration document for Charity Golf Day 2022

The project requires 2 documents to be updated to look more graphically savvy and professionally presentable.
1. Charity golf day sponsorship document
2. One page registration document.
The text has been completed. Text not to be changed - just graphics.
New images would be preferred.
The logos have been provided.

Target Market(s)

Corporate Sponsors and Golf players

Requirements
Must have
• Golf Theme

```html
<!DOCTYPE html>
<html lang="en">
<head>
<meta charset="utf-8">
<title>Charity Golf Day – Sponsorship Proposal</title>
<link href="https://fonts.googleapis.com/css2?family=Montserrat:wght@300;400;500;600;700&display=swap" rel="stylesheet">
<style>
:root{
  --navy:#1f4a8e;
  --orange:#f0a032;
  --ink:#2c2c2c;
  --board:#48484a;
  --paper:#ffffff;
  --green:#6f9a3a;
}
*{box-sizing:border-box;margin:0;padding:0}
html,body{width:1200px;height:1200px;overflow:hidden;background:var(--board)}
body{font-family:'Montserrat',sans-serif;color:var(--ink)}
.board{position:absolute;left:0;top:0;width:1932px;height:1932px;transform:scale(0.62112);transform-origin:0 0}
.page{position:absolute;background:var(--paper);overflow:hidden}
.page svg.art{position:absolute;left:0;top:0}
.band{position:absolute;left:30px;top:25px;display:flex;height:28px}
.band span{display:block;color:#fff;font-size:19px;font-weight:400;line-height:28px;padding:0 8px;letter-spacing:.3px}
.band .b-navy{background:var(--navy)}
.band .b-orange{background:var(--orange)}
.page-no{position:absolute;right:22px;bottom:16px;font-size:8px}
.body{position:absolute;font-size:9px;line-height:1.3}
.h-blue{color:var(--navy);font-weight:400}
.orange{color:var(--orange)}
.navy{color:var(--navy)}
.bold{font-weight:700}
ul.dots{list-style:none}
ul.dots li{position:relative;padding-left:8px;margin-bottom:5px}
ul.dots li::before{content:"•";position:absolute;left:0}
ul.odots li::before{color:var(--orange)}
/* cover */
.brand-name{position:absolute;left:30px;top:30px;color:var(--navy);font-size:32px;font-weight:600;line-height:1}
.brand-sub{position:absolute;left:15px;top:70px;color:var(--navy);font-size:19px;font-weight:400}
.brand-dot{position:absolute;left:137px;top:20px;width:60px;height:60px;border-radius:50%;background:var(--orange)}
.cover-title{position:absolute;left:248px;top:20px;line-height:1.05}
.cover-title .t1{color:var(--navy);font-size:26px;font-weight:700}
.cover-title .t2{color:var(--orange);font-size:25px;font-weight:400}
.cover-title .t3{color:var(--navy);font-size:25px;font-weight:400}
.cover-proposal{position:absolute;left:277px;top:558px;color:#fff;font-size:24px;font-weight:600;line-height:1.05;letter-spacing:.5px}
.cover-foot{position:absolute;left:14px;top:622px;font-size:9.5px;line-height:1.3;color:#222}
.web{position:absolute;font-size:11px;font-weight:700;color:#222;display:flex;align-items:center;gap:5px}
/* contents */
.sec-title{color:var(--orange);font-size:20px;font-weight:400}
.toc{position:absolute;left:40px;top:100px;width:390px;font-size:9.5px}
.toc div{display:flex;justify-content:space-between;height:20.5px}
.toc-rule{position:absolute;left:365px;top:98px;width:2px;height:132px;background:var(--navy)}
.contact{position:absolute;font-size:9.5px;line-height:1.3}
.contact .nm{color:var(--navy);font-weight:700;font-size:10.5px}
/* sponsorship */
.pill{display:inline-block;color:#fff;border-radius:12px;padding:1px 10px;font-size:14px;font-weight:500}
.pill.gold{background:var(--navy)}
.pill.silver{background:var(--orange)}
.form-row{border-bottom:1px dotted #666;display:flex;font-size:11px;font-weight:700;color:#222;height:16px;align-items:flex-end}
.form-sub{font-size:8.5px;font-weight:400;border-bottom:1px dotted #666;height:14px;margin-top:6px}
</style>
</head>
<body>
<div class="board">

  <!-- Page 1: cover -->
  <section class="page" style="left:110px;top:243px;width:530px;height:683px">
    <svg class="art" width="530" height="683" viewBox="0 0 530 683">
      <defs>
        <linearGradient id="g-golfer" x1="0" y1="0" x2="0" y2="1">
          <stop offset="0" stop-color="#f4ecd6"/>
          <stop offset=".45" stop-color="#d8cfa6"/>
          <stop offset="1" stop-color="#8fa748"/>
        </linearGradient>
        <radialGradient id="g-ball" cx=".5" cy=".45" r=".6">
          <stop offset="0" stop-color="#c7d78c"/>
          <stop offset=".6" stop-color="#7ea63d"/>
          <stop offset="1" stop-color="#3f6a22"/>
        </radialGradient>
      </defs>
      <circle cx="275" cy="400" r="282" fill="url(#g-golfer)" role="img" aria-label="Photo of a golfer mid-swing on a sunny fairway"/>
      <circle cx="375" cy="385" r="210" fill="var(--navy)"/>
      <circle cx="395" cy="360" r="172" fill="var(--orange)"/>
      <circle cx="410" cy="350" r="145" fill="url(#g-ball)" role="img" aria-label="Close-up photo of a golf ball on a tee beside a driver"/>
    </svg>
    <div class="brand-name">Lantern</div>
    <div class="brand-sub">Westbrook</div>
    <div class="brand-dot"></div>
    <div class="cover-title">
      <div class="t1">CHARITY GOLF DAY</div>
      <div class="t2">Friday 25 March 2022</div>
      <div class="t3">Elmcroft Golf Club</div>
    </div>
    <div class="cover-proposal">SPONSORSHIP<br>PROPOSAL</div>
    <div class="cover-foot"><b>Supporting Prostate Cancer Research</b><br>Help us hit prostate cancer off the green and beat<br>the most common cancer in Australian men.</div>
    <div class="web" style="left:336px;top:646px">
      <svg width="11" height="11" viewBox="0 0 12 12"><circle cx="6" cy="6" r="5" fill="none" stroke="#222"/><ellipse cx="6" cy="6" rx="2.2" ry="5" fill="none" stroke="#222"/><line x1="1" y1="6" x2="11" y2="6" stroke="#222"/></svg>
      www.lcw.org.au/golf-day</div>
  </section>

  <!-- Page 2: contents -->
  <section class="page" style="left:682px;top:243px;width:536px;height:687px">
    <svg class="art" width="536" height="687" viewBox="0 0 536 687">
      <defs>
        <linearGradient id="g-putt" x1="0" y1="0" x2="0" y2="1">
          <stop offset="0" stop-color="#f3e6c4"/>
          <stop offset=".5" stop-color="#b9b978"/>
          <stop offset="1" stop-color="#4f8a2a"/>
        </linearGradient>
        <linearGradient id="g-green" x1="0" y1="0" x2="0" y2="1">
          <stop offset="0" stop-color="#e8b6a0"/>
          <stop offset=".45" stop-color="#7c9a4a"/>
          <stop offset="1" stop-color="#3f7a22"/>
        </linearGradient>
      </defs>
      <circle cx="160" cy="590" r="170" fill="url(#g-putt)" role="img" aria-label="Photo of a golfer putting towards the hole at sunset"/>
      <circle cx="251" cy="449" r="35" fill="var(--orange)"/>
      <circle cx="462" cy="496" r="110" fill="var(--navy)"/>
      <circle cx="415" cy="460" r="90" fill="url(#g-green)" role="img" aria-label="Photo of a golf ball resting on the green"/>
    </svg>
    <div class="band"><span class="b-navy">CHARITY GOLF DAY</span><span class="b-orange">SPONSORSHIP PROPOSAL</span></div>
    <div class="sec-title" style="position:absolute;left:38px;top:60px">Contents</div>
    <div class="toc">
      <div><span>Charity Golf Day Invitation</span><span>2</span></div>
      <div><span>About Prostate Cancer</span><span>3</span></div>
      <div><span>Why are we asking you to be involved</span><span>3</span></div>
      <div><span>What to expect</span><span>4</span></div>
      <div><span>Sponsorship Opportunities</span><span>5</span></div>
      <div><span>Application Form</span><span>7</span></div>
    </div>
    <div class="toc-rule"></div>
    <div class="sec-title" style="position:absolute;left:38px;top:257px">Contact</div>
    <div class="contact" style="left:40px;top:290px">
      <div class="nm">Maren (Ellis) Ward</div>
      Convenor<br>Co - President, Lantern Club of Westbrook<br>Mobile: 0400 555 019<br>Email: marenward@mailbox.example<br>Web: www.lcw.org.au/golf-day
    </div>
    <div class="contact" style="left:318px;top:290px">
      <div class="nm">Tessa Corvin</div>
      Event Manager<br>Email: tessa.corvin@netmail.example
    </div>
    <div class="web" style="left:340px;top:652px">
      <svg width="11" height="11" viewBox="0 0 12 12"><circle cx="6" cy="6" r="5" fill="none" stroke="#222"/><ellipse cx="6" cy="6" rx="2.2" ry="5" fill="none" stroke="#222"/><line x1="1" y1="6" x2="11" y2="6" stroke="#222"/></svg>
      www.lcw.org.au/golf-day</div>
  </section>

  <!-- Page 3: invitation letter -->
  <section class="page" style="left:1257px;top:243px;width:534px;height:687px">
    <div class="band"><span class="b-navy">CHARITY GOLF DAY</span><span class="b-orange">SPONSORSHIP PROPOSAL</span></div>
    <div class="body" style="left:38px;top:68px;width:466px">
      <p class="navy" style="font-size:9.5px;margin-bottom:16px">Join us for an exclusive day on the private Elmcroft Golf Course, with all proceeds going to support Prostate Cancer Research, Awareness and Support.</p>
      <p style="margin-bottom:10px">The Lantern Club of Westbrook will again be holding its Charity Golf Day with all proceeds used to support the Prostate Cancer Research, awareness and Support Programs. The venue will be the prestigious Elmcroft Golf Club on Friday 25 March 2022, with a shotgun start at 8:00 am.</p>
      <p style="margin-bottom:14px">We have enclosed for your information a copy of our promotional sponsor packages that outline the event, sponsorship package options and inclusions.</p>
      <p style="margin-bottom:16px">The format of the day involves :</p>
      <div style="padding-left:12px">
        <p style="margin-bottom:9px"><svg width="12" height="10" viewBox="0 0 12 10" style="vertical-align:-2px;margin-right:6px"><path d="M1 5 L4.5 9 L11 1" fill="none" stroke="var(--navy)" stroke-width="2"/></svg>Player registration, refreshments and light breakfast from 7:00am</p>
        <p style="margin-bottom:9px"><svg width="12" height="10" viewBox="0 0 12 10" style="vertical-align:-2px;margin-right:6px"><path d="M1 5 L4.5 9 L11 1" fill="none" stroke="var(--navy)" stroke-width="2"/></svg>Ambrose competition starting at 8:00am</p>
        <p style="margin-bottom:24px"><svg width="12" height="10" viewBox="0 0 12 10" style="vertical-align:-2px;margin-right:6px"><path d="M1 5 L4.5 9 L11 1" fill="none" stroke="var(--navy)" stroke-width="2"/></svg>Two Course lunch and presentations in the club house from 12:30pm</p>
      </div>
      <p style="margin-bottom:10px">Your commitment to supporting health programs in our community is truly appreciated. With assistance from sponsors such as yourself, we will continue to see improvements in the support and treatment for men and their families with prostate cancer.</p>
      <p style="margin-bottom:10px">We hope that you will consider supporting the worthwhile event that is open to any organisation or individual who wishes to enjoy the benefits of playing golf at the prestigious Elmcroft Golf Club.</p>
      <p style="margin-bottom:28px">For more information, please check the website ( <span class="navy">www.lcw.org.au/golf-day</span>) or should you wish to discuss any aspect of the event, please contact me on <b class="navy">0400 555 019.</b></p>
      <p style="margin-bottom:8px">Yours sincerely</p>
      <div role="img" aria-label="Handwritten signature" style="width:62px;height:14px;background:#e6e3f3;margin-bottom:60px"></div>
      <p><b class="navy" style="font-size:10px">Maren (Ellis) Ward</b><br>Convener<br>Co - President 2021 -2022<br>Secretary 2021 - 2022<br>Lantern Club of Westbrook</p>
    </div>
    <div class="page-no">Page 2</div>
  </section>

  <!-- Page 4: why prostate cancer -->
  <section class="page" style="left:97px;top:1022px;width:543px;height:698px">
    <svg class="art" width="543" height="698" viewBox="0 0 543 698">
      <defs>
        <linearGradient id="g-clinic" x1="0" y1="0" x2="1" y2="1">
          <stop offset="0" stop-color="#eef1f4"/>
          <stop offset=".5" stop-color="#c9d6e0"/>
          <stop offset="1" stop-color="#dfe6eb"/>
        </linearGradient>
      </defs>
      <circle cx="470" cy="350" r="95" fill="url(#g-clinic)" role="img" aria-label="Photo of a doctor consulting a male patient"/>
      <circle cx="460" cy="545" r="152" fill="url(#g-clinic)" role="img" aria-label="Photo of a light blue awareness ribbon beside the words Prostate Cancer"/>
    </svg>
    <div class="band" style="top:26px"><span class="b-navy">CHARITY GOLF DAY</span><span class="b-orange">SPONSORSHIP PROPOSAL</span></div>
    <div class="body" style="left:29px;top:64px;width:470px;font-size:9.2px">
      <div class="h-blue" style="font-size:15px;margin-bottom:6px">Why prostate cancer?</div>
      <ul class="dots" style="margin-bottom:8px">
        <li style="margin-bottom:3px">Prostate cancer is the most diagnosed cancer in Australian men.</li>
        <li style="margin-bottom:3px">Approximately 20,000 Australian men are diagnosed with prostate cancer each year.</li>
        <li style="margin-bottom:3px">Over 200,000 Australian men are living with a diagnosis prostate cancer.</li>
        <li style="margin-bottom:3px">95% of Australian men diagnosed with prostate cancer survive for at least 5 years.</li>
        <li style="margin-bottom:3px">Almost 3,500 Australian men die of prostate cancer each year.</li>
      </ul>
      <div class="h-blue" style="font-size:15px;margin-bottom:6px">Why are we asking you to be involved?</div>
      <ul class="dots" style="margin-bottom:8px">
        <li style="margin-bottom:3px">Every day 54 Australian men will be told they have prostate cancer</li>
        <li style="margin-bottom:3px">70% of research applications are unfunded</li>
        <li style="margin-bottom:3px">1 in 6 men will suffer from prostate cancer</li>
        <li style="margin-bottom:3px">9 families lose a loved one to prostate cancer every day</li>
        <li style="margin-bottom:3px">Only 1 in 3 men have access to a specialist nurse</li>
      </ul>
      <div class="h-blue" style="font-size:15px;margin-bottom:6px">What this fundraising event can achieve</div>
      <ul class="dots odots" style="width:340px;margin-bottom:10px">
        <li style="margin-bottom:8px"><b class="orange">$12,500</b> – Could provide funding for a researcher working for one month on a project to reduce side – effects post treatment.</li>
        <li style="margin-bottom:8px"><b class="orange">$30,000</b> – could provide finding for a senior scientist for three months working on a project to improve treatments for prostate cancer that has spread to the bones.</li>
        <li style="margin-bottom:8px"><b class="orange">$50,000</b> – could fund a project to improve early - diagnosis for men with a family history of prostate cancer.</li>
      </ul>
      <p style="width:290px;margin-bottom:12px">Proceeds from this event will be donated to Prostate Cancer Research Group at the Life Sciences Discovery Institute, Harbourview University, to fund world leading, innovative research and to support men and their families affected by prostate cancer.</p>
      <p style="width:295px;margin-bottom:12px">Their innovative research program has a strong translational approach, involving lab-based studies with tissues donated by patients with prostate cancer. Their collaborative studies with clinicians and patient advocates address questions that are relevant to patient care. The findings have the potential to improve the management and outcomes of men with different stages of prostate cancer. Recent studies have informed international guidelines for diagnosis of prostate cancer and led to new clinical trials.</p>
      <p style="width:330px">For more information visit their website <span class="navy">www.harbourview.edu/discovery-institute/prostate-research-group</span></p>
    </div>
    <div class="page-no">Page 3</div>
  </section>

  <!-- Page 5: what to expect + sponsorship -->
  <section class="page" style="left:675px;top:1021px;width:545px;height:700px">
    <div class="band"><span class="b-navy">CHARITY GOLF DAY</span><span class="b-orange">SPONSORSHIP PROPOSAL</span></div>
    <div class="body" style="left:24px;top:58px;width:500px;font-size:8px">
      <div style="text-align:center;color:var(--navy);font-weight:700;font-size:15px">Friday 25 March 2022 at Elmcroft Golf Club</div>
      <p style="text-align:center;margin-bottom:14px">The Championship Par 72 layout of 6179 metres is a genuine test to all standards of players.<br>Situated only 15 minutes from the city, the course meanders along the Alder River providing a beautiful vista and is home for 100's of species of native birds and tall-established trees.</p>
      <div style="display:flex;margin-bottom:16px">
        <div style="width:152px"><div class="navy" style="font-size:11px;font-weight:500;margin:6px 0 10px 4px">Breakfast :</div><ul class="dots"><li>Light Breakfast</li><li>Tea and coffee</li></ul></div>
        <div style="width:162px"><div class="navy" style="font-size:11px;font-weight:500;margin:6px 0 10px 0">Lunch :</div><ul class="dots"><li>Two-Course Lunch</li><li>Drinks at Bar Prices</li></ul></div>
        <div><div class="navy" style="font-size:11px;font-weight:500;margin-bottom:6px">Schedule :</div>
          <div style="display:grid;grid-template-columns:52px auto;row-gap:1px;padding-left:2px">
            <span>7:00am to 7.30am:</span><span style="padding-left:18px">Registration</span>
            <span>7:15am:</span><span>Breakfast</span><span>7:45am:</span><span>Player Briefing</span>
            <span>8:00am:</span><span>Shotgun start</span><span>12.30pm:</span><span>Lunch, Presentation/Prizes</span>
            <span>3.00pm:</span><span>Finish</span></div></div>
      </div>
      <div class="navy" style="font-size:11px;font-weight:500;margin-bottom:4px">What else to expect :</div>
      <p style="margin-bottom:5px">4-person Ambrose</p>
      <ul class="dots" style="margin-bottom:14px">
        <li style="margin-bottom:7px">On course competitions such as nearest the pins and longest drive</li>
        <li style="margin-bottom:7px">Trophies &amp; Prizes</li>
        <li style="margin-bottom:7px">On the day you will have access to practice putting, chipping greens, and driving range</li>
        <li style="margin-bottom:7px">A refreshment cart will circulate the golf course for players to purchase refreshments at own cost</li>
        <li style="margin-bottom:7px">Hire Equipment
          <ul class="dots" style="margin-top:7px;padding-left:4px"><li style="margin-bottom:7px">Hire sets (Standard) $35.00 per set; (Premium) $50.00 per set</li><li style="margin-bottom:7px">Hire shoes $10.00 per pair</li><li>Carts $40.00 each (Booking essential as numbers are limited, but it is an easy course to walk)</li></ul></li>
      </ul>
      <div class="navy" style="font-size:15px;font-weight:500;margin-bottom:4px">Sponsorship Opportunities</div>
      <div style="display:flex;gap:26px;font-size:7.6px;line-height:1.2">
        <div style="width:248px">
          <span class="pill gold">Gold $5,000</span>
          <p style="margin:3px 0 2px">The Gold Sponsor is entitled to the following :</p>
          <ul class="dots">
            <li style="margin-bottom:1px">Event naming rights</li>
            <li style="margin-bottom:1px">Eight (8) representatives playing in the event, including all green fees, four (4) carts, light breakfast &amp; 2 course lunch</li>
            <li style="margin-bottom:1px">Your company signage / banners displayed exclusively at club entrance and social area.</li>
            <li style="margin-bottom:1px">Your logo and your company information on all promotional and marketing material being used on the day including our website, email to database and our social media channels.</li>
            <li style="margin-bottom:1px">A Banner with company logo on the first hole</li>
            <li style="margin-bottom:1px">Opportunity to say a few words at the beginning of the game as the chief sponsor of the event.</li>
            <li style="margin-bottom:1px">Your company merchandise on display.</li>
            <li style="margin-bottom:1px">Presenting the winners awards</li>
            <li style="margin-bottom:1px">Free advertising in our Lantern Club Newsletter, website, and social media channels for 12 months.</li>
            <li style="margin-bottom:1px">Opportunity to "capture" prospective clients on the day</li>
            <li style="margin-bottom:1px">Great Publicity: Be seen as being associated with an excellent cause</li>
          </ul>
        </div>
        <div style="width:220px">
          <span class="pill silver">Silver $2,500</span>
          <p style="margin:3px 0 2px">The Silver Sponsor is entitled to the following :</p>
          <ul class="dots odots">
            <li style="margin-bottom:4px">Four (4) representatives playing in the event, including all green fees, two (2) carts, light breakfast &amp; 2 course lunch</li>
            <li style="margin-bottom:4px">Exclusive banner with your company logo on a tee of choice (except hole 1)</li>
            <li style="margin-bottom:4px">Opportunity to say a few words as a major sponsor</li>
            <li style="margin-bottom:4px">Your company merchandise on display.</li>
            <li style="margin-bottom:4px">Your logo and your company information on all promotional and marketing material being used on the day including our website, email to database and our social media channels.</li>
            <li style="margin-bottom:4px">Free advertising in our Lantern Club Newsletter, website, and social media channels for 6 months.</li>
            <li style="margin-bottom:4px">Opportunity to "capture" prospective clients on the day</li>
            <li>Great Publicity: Be seen as being associated with an excellent cause</li>
          </ul>
        </div>
      </div>
    </div>
    <div class="page-no">Page 4</div>
  </section>

  <!-- Page 6: team registration -->
  <section class="page" style="left:1253px;top:1014px;width:548px;height:706px">
    <div class="band" style="top:26px"><span class="b-navy">CHARITY GOLF DAY</span><span class="b-orange">SPONSORSHIP PROPOSAL</span></div>
    <div style="position:absolute;left:32px;top:66px;background:var(--navy);color:#fff;font-size:14px;font-weight:500;padding:0 12px;border-radius:10px;line-height:18px">Team Name:</div>
    <div class="body" style="left:38px;top:88px;width:478px">
      <div class="form-row">Player 1 :</div><div class="form-sub">Official NG H/Cap :</div>
      <div class="form-row" style="margin-top:30px">Player 2 :</div><div class="form-sub">Official NG H/Cap :</div>
      <div class="form-row" style="margin-top:30px">Player 3 :</div><div class="form-sub">Official NG H/Cap :</div>
      <div class="form-row" style="margin-top:30px">Player 4 :</div><div class="form-sub">Official NG H/Cap :</div>
      <p class="navy bold" style="font-size:8.5px;margin:14px 0 18px">Please Note: Any player without an official NG H/Cap will be given a maximum handicap of 27 (Males) &amp; 36 (Females).</p>
      <div class="form-row">Player 5 :</div><div class="form-sub">Official NG H/Cap :</div>
      <div class="form-row" style="margin-top:26px">Player 6 :</div><div class="form-sub">Official NG H/Cap :</div>
      <div class="form-row" style="margin-top:30px">Player 7 :</div><div class="form-sub">Official NG H/Cap :</div>
      <div class="form-row" style="margin-top:24px">Player 8 :</div><div class="form-sub">Official NG H/Cap :</div>
      <p class="navy bold" style="font-size:8.5px;margin:22px 0 8px">Please Note: Any player without an official NG H/Cap will be given a maximum handicap of 27 (Males) &amp; 36 (Females).</p>
      <div style="border:1px solid #555;padding:4px 3px;font-size:6.6px;line-height:1.25;width:456px">
        <div class="navy" style="font-size:8.5px;font-weight:500;margin-bottom:4px">Cancellation Terms</div>
        If the organiser cancels the event prior to the scheduled date, the sponsor is entitled to a 100% refund. If the event is rescheduled by the organiser, and the player or sponsor can reasonably demonstrate their inability to participate they will be entitled to a full refund. In the event of a player or sponsor cancellation, the Lantern Club of Westbrook reserves the right to retain monies paid in full unless resold. Any cancellations must be advised in writing via email to the Convenor Maren Ward (marenward@mailbox.example).
      </div>
    </div>
    <div class="page-no">Page 6</div>
  </section>

</div>
</body>
</html>
```